■要望
デザイン>HPの導線整理
HPの見た目の印象をよくすることで「ここへ行ってみようかな」という気持ちを引き出したいです。
なので、リニューアルにあたって一番の要望はデザイン性の向上としました。

■現在のサイトの問題点
・見づらい
スッキリとシンプルな構成にしてください。

・内装とあったデザインになっていない
内装は茶色・緑・クリーム色なのですが、現行サイトはテイストが異なっております。
内装とそろえたデザインにしたいので添付ファイルをご参照の上ご応募ください。

■強み
・患者さまの症状、状況にあわせた最適なプランを提供するのがウリ
価格帯は比較的安価ですが、安さをウリにしているわけではありませんので
商売っ気が強く見えるのは避けたいです。

・特定の特化した施術は宣伝していない。
特定の施術を目玉商品とするわけではなく、
大量のメニューの中から最適なメニューを組めるようにしています。

■HPに望む効果
・新規顧客
リピーター獲得の取り組みはTALQでやっておりますので、
HPサイトのターゲットは新規顧客に絞ります。

■HPのメインターゲット
・30~40代(特に主婦層)
現在の患者層は高齢者層がメインです。
その層はキープしつつ、もう少し若い年代を増やすために
HPのターゲットは30~40代と設定しました。

主婦層がメイン属性ですが、子連れの方や仕事で疲れている会社員の方も視野にいれております。

■軸となっている施術
店舗名には「鍼灸整骨院」と入っておりますが
軸となる施術は整体で、そこへ鍼灸が付随している形です。

■カラー
全体的にアースカラーでお願いします。
・メインカラー:白やクリーム色
・アクセントカラー:緑、土色
カラーの配分はお任せいたします。

ライトグレイッシュトーン、ライトトーンを使用した
明るくも落ち着いたデザインを希望します。

※NGカラー:黄色、青

■テイスト
・ナチュラル、優しい、あたたかい
※NGテイスト:派手、エレガント、幻想的・神秘的

■希望イメージ

・明るくてシンプルで落ち着きのあるデザイン
・親しみやすさを出してほしい(低価格っぽさはNG)
・落ち着いた年代の女性に受けそうなテイスト

■登録しているSNS
Picturely、TALQ、Friendvio

■参考サイト
http://kurose-wqs.com/
シンプルかつ分かりやすく印象的です。

http://mistvale-circle.com
構成が分かりやすく、女性ウケもよさそうです。

■サイトマップ
①TOP
L②当院について
L③施術メニューと料金
L④首・肩の痛みにお悩みの方へ
L⑤取れない疲れにお悩みの方へ
L⑥不眠にお悩みの方へ
L⑦腰痛でお悩みの方へ
L⑧体幹を鍛えたい方へ
L⑨交通事故治療
L⑩オーダオーメイド枕で快適な睡眠を
L⑪自費治療
L⑫鍼灸治療
L⑬患者さまの声
L⑭よくあるご質問
L⑮お問い合わせ
L⑯ブログ(詳細)
L⑰ブログ(一覧)
L⑱お知らせ(詳細)
L⑲お知らせ(一覧)

※※※ご注意いただきたい点につきまして※※※
【店舗へのご連絡はおやめください】
ワークモールの規約にもありますが、店舗様の通常業務に支障が出るため・素材について
直接電話等のお問い合わせをお控えいただきますよう、ご協力の程お願いいたします。

※※※※※※※※※※※※※※※※※※※※※※

ご不明点などございましたらいつでも
ワークモール内メッセージフォームにてお問い合わせください。

皆さまのアイデアをお待ちしております!

何卒よろしくお願い申し上げます。

https://tomoki-seiryo.com/
【撮影素材】
ダウンロードリンク:
http://boxdrift-share.com/download/7ab29c64e18d03f5b7a1c92e6d0f4b8833c1a07d
パスワード:「tomoki」

【その他素材はImagoraかその他無償の素材をご使用ください】
素材として必要なものがある場合にはイマゴラ画像をご使用ください。
疑問や不明点などがありましたら、ワークモール内メッセージにて頂戴できますと幸いです。

その際、定期契約でダウンロード出来る画像のみを使用してください。
(画像検索した際に出てくるサムネール下の画像番号の横に
イマゴラのマークがあるものは使用しないようお願いいたします。)

イマゴラ以外の素材を使用する際には、
必ず無料で提供いただける物のみご使用ください。
もう少し提案が見たいため、延長させて頂きます。

```html
<!DOCTYPE html>
<html lang="ja">
<head>
<meta charset="utf-8">
<title>ともき鍼灸院・整骨院</title>
<link href="https://fonts.googleapis.com/css2?family=Noto+Serif+JP:wght@400;600&family=Noto+Sans+JP:wght@400;500;700&display=swap" rel="stylesheet">
<style>
:root{
  --cream:#f8f0e1;
  --white:#ffffff;
  --tan:#d6a46a;
  --tan-dark:#b7824a;
  --brown:#6e4f33;
  --text:#4a3a2c;
  --muted:#8b7a68;
  --green:#8db263;
  --line:#e4d3b7;
  --photo-room:#e9ddd0;
  --photo-skin:#e8cdb6;
}
*{box-sizing:border-box;margin:0;padding:0}
html,body{width:1200px;height:3524px;overflow:hidden}
body{font-family:"Noto Sans JP",sans-serif;color:var(--text);background:var(--white);font-size:14px;line-height:1.7}
.photo{display:block}
.nowrap{white-space:nowrap}

/* hero */
.hero{position:relative;height:380px}
.hero-photo{position:absolute;inset:0;background:linear-gradient(100deg,#efe4d6 0%,#f6efe6 45%,#e4d5c4 100%)}
.hero-copy{position:absolute;right:70px;top:50px;width:420px;background:rgba(255,255,255,.55);padding:26px 30px}
.hero-copy p{font-family:"Noto Serif JP",serif;font-size:30px;line-height:1.55;color:var(--brown);white-space:nowrap}
.hero-copy .accent{color:var(--tan-dark)}
.hero-copy .green{color:var(--green)}
.hero-badges{position:absolute;right:90px;top:250px;display:flex;gap:22px}
.badge{width:92px;height:92px;border-radius:50%;background:var(--tan);color:#fff;display:flex;align-items:center;justify-content:center;text-align:center;font-size:13px;line-height:1.4;font-weight:500}

/* header + intro */
.header{display:flex;align-items:center;padding:14px 60px 0;height:50px}
.logo{font-family:"Noto Serif JP",serif;font-size:24px;color:var(--brown);font-weight:600;display:flex;align-items:center;gap:10px;white-space:nowrap}
.logo .mark{width:14px;height:14px;background:var(--tan);flex:none}
.nav{margin-left:auto;display:flex;font-size:13px}
.nav a{color:var(--text);text-decoration:none;padding:8px 18px;border-left:1px solid var(--line);white-space:nowrap}
.nav a:first-child{background:var(--cream);border-left:none}
.intro{display:flex;padding:24px 60px 0;gap:40px;height:170px}
.intro-lead{width:300px;font-size:14px;line-height:1.9;font-weight:500}
.intro-body{flex:1;font-size:12.5px;color:var(--muted);line-height:1.9}
.intro-art{width:150px;height:120px;background:var(--cream);border-radius:8px}
.more-btn{display:inline-block;border:1px solid var(--tan);color:var(--brown);font-size:12px;padding:6px 36px;background:#fff;white-space:nowrap}

/* section title */
.sec-title{text-align:center;font-family:"Noto Serif JP",serif;font-size:28px;color:var(--brown);letter-spacing:.1em;line-height:1.4}
.sec-sub{text-align:center;font-size:13px;color:var(--muted);margin-top:6px}
.center{text-align:center;margin-top:26px}

/* menu */
.menu{background:var(--cream);padding:40px 0 0;height:780px;overflow:hidden}
.menu-grid{width:930px;margin:26px auto 0;display:grid;grid-template-columns:repeat(3,1fr);gap:24px}
.card{display:flex;height:140px}
.card .photo{width:130px;height:140px;flex:none;background:linear-gradient(135deg,var(--photo-skin),var(--photo-room))}
.card-body{flex:1;background:var(--tan);color:#fff;padding:12px}
.card-body h3{font-size:14px;font-weight:700;border-bottom:1px solid rgba(255,255,255,.6);padding-bottom:4px;margin-bottom:6px;white-space:nowrap}
.card-body p{font-size:11px;line-height:1.6}

/* contact banner */
.contact-banner{width:820px;margin:30px auto 0;border:2px solid var(--tan);background:#fff;display:flex;height:110px}
.cb-name{width:240px;flex:none;background:var(--tan);color:#fff;padding:24px 18px;font-family:"Noto Serif JP",serif;white-space:nowrap}
.cb-name .n{font-size:19px;line-height:1.4}
.cb-name .s{font-size:11px;font-family:"Noto Sans JP",sans-serif;margin-top:6px}
.cb-main{flex:1;padding:12px 18px;display:flex;gap:16px;align-items:center;justify-content:space-between}
.cb-hours{font-size:11px;color:var(--muted);line-height:1.6;white-space:nowrap}
.cb-tel{display:flex;align-items:center;gap:6px;color:var(--tan-dark);font-size:24px;font-weight:700;white-space:nowrap;line-height:1.3}
.cb-photo{width:140px;flex:none;height:106px;background:linear-gradient(135deg,#d9cbb9,#efe6da)}
.cb-btns{display:flex;flex-direction:column;gap:8px}
.cb-btn{background:var(--tan);color:#fff;font-size:12px;padding:5px 14px;text-align:center;white-space:nowrap}

/* concerns */
.concerns{height:600px;background:linear-gradient(180deg,#f3efec,#ebe4de);padding-top:56px}
.concern-row{display:flex;justify-content:center;gap:34px;margin-top:34px}
.concern{text-align:center;font-size:13px}
.concern .photo{width:210px;height:140px;background:linear-gradient(135deg,var(--photo-skin),#efe8e2);margin-bottom:8px}

/* voices */
.voices{height:680px;padding-top:50px;background:var(--white)}
.voice-box{width:720px;margin:24px auto 0;border:1px solid var(--tan);padding:16px 24px}
.voice-box h3{font-size:14px;color:var(--brown);border-bottom:1px dashed var(--line);padding-bottom:6px;margin-bottom:8px}
.voice-box p{font-size:12px;color:var(--muted);line-height:1.8}
.voice-people{display:flex;justify-content:center;gap:90px;margin-top:36px}
.voice-people .photo{width:130px;height:130px;border-radius:50%;background:linear-gradient(135deg,var(--photo-skin),var(--photo-room))}

/* blog news */
.posts{display:flex;justify-content:center;gap:90px;padding-top:40px;height:340px}
.post-col{width:380px}
.post-col h2{text-align:center;font-family:"Noto Serif JP",serif;font-size:22px;color:var(--brown);margin-bottom:12px}
.post-col li{list-style:none;font-size:12px;border-bottom:1px dotted var(--line);padding:5px 0;display:flex;gap:16px;white-space:nowrap}
.post-col li span{color:var(--tan-dark)}
.post-col .center{margin-top:18px}

/* access */
.access{display:flex;justify-content:center;gap:60px;height:280px;padding-top:10px}
.access-card{width:380px;border:2px solid var(--tan);padding:18px;height:250px}
.access-tel{display:flex;align-items:center;gap:8px;color:var(--tan-dark);font-size:26px;font-weight:700;justify-content:center;white-space:nowrap}
.hours{width:100%;border-collapse:collapse;margin-top:12px;font-size:11px}
.hours th,.hours td{border:1px solid var(--line);padding:4px;text-align:center;white-space:nowrap}
.hours th{background:var(--tan);color:#fff;font-weight:500}
.map{width:380px;height:250px;background:linear-gradient(135deg,#eceae4,#dfe3dc)}

/* footer */
.footer{background:var(--cream);height:254px;padding:26px 100px 0;display:flex;gap:50px;position:relative}
.f-info{width:300px;flex:none;font-size:12px;color:var(--muted);line-height:1.6}
.f-info .logo{font-size:22px;margin-bottom:8px}
.f-btn{display:inline-block;border:1px solid var(--tan);background:#fff;color:var(--brown);padding:4px 20px;margin-top:8px;font-size:12px}
.f-talq{display:flex;align-items:center;gap:8px;margin-top:8px;color:var(--green);font-weight:700}
.f-talq i{width:14px;height:14px;background:var(--green);display:block}
.f-links{display:grid;grid-template-columns:repeat(3,170px);gap:2px 10px;font-size:12px;margin-top:10px;align-content:start}
.f-links a{color:var(--text);text-decoration:none;white-space:nowrap;line-height:1.9}
.f-social{display:flex;flex-direction:column;gap:4px;margin-top:10px;font-size:12px;color:var(--brown)}
.copy{position:absolute;left:0;bottom:0;width:100%;height:30px;background:var(--brown);color:#fff;text-align:center;font-size:11px;line-height:30px}
</style>
</head>
<body>

<section class="hero">
  <div class="hero-photo photo" role="img" aria-label="明るい施術室の室内写真"></div>
  <div class="hero-copy">
    <p><span class="accent">健康を支える根源。</span><br>肩こり・腰痛の原因、<br><span class="green">筋肉、骨格、神経を改善</span></p>
  </div>
  <div class="hero-badges">
    <div class="badge">予約優先<br>制</div>
    <div class="badge">平日20時<br>まで受付</div>
    <div class="badge">各種保険<br>取扱い</div>
  </div>
</section>

<header class="header">
  <div class="logo"><span class="mark"></span>ともき鍼灸院・整骨院</div>
  <nav class="nav">
    <a href="#">当院について</a><a href="#">施術メニュー・料金</a><a href="#">患者様の声</a><a href="#">よくあるご質問</a><a href="#">アクセス</a><a href="#">お問い合わせ</a>
  </nav>
</header>
<section class="intro">
  <p class="intro-lead">ともき鍼灸院・整骨院では、<br>患者さまお一人おひとりに合わせた<br>施術方法をご提案します。</p>
  <div class="intro-body">
    <p>首こり、腰痛、慢性的な疲れなど体のお悩みはお気軽にご相談ください。症状や生活習慣を丁寧にうかがい、豊富なメニューの中から最適な施術を組み合わせます。はじめての方も安心してお越しいただけるよう、落ち着いた空間でお待ちしております。</p>
    <div style="text-align:center;margin-top:14px"><span class="more-btn">詳しくはこちら</span></div>
  </div>
  <div class="intro-art" role="img" aria-label="施術者のやさしいイラスト"></div>
</section>

<section class="menu">
  <h2 class="sec-title">施術メニュー</h2>
  <p class="sec-sub">豊富な施術メニューの中からご提案いたします。お気軽にご相談ください。</p>
  <div class="menu-grid">
    <div class="card"><div class="photo" role="img" aria-label="整体施術の写真"></div><div class="card-body"><h3>症状別コース</h3><p>首・肩・腰の痛みや疲れなど症状に合わせて施術します。</p></div></div>
    <div class="card"><div class="photo" role="img" aria-label="鍼灸施術の写真"></div><div class="card-body"><h3>鍼灸治療</h3><p>体の内側から整える鍼とお灸で自然な回復を促します。</p></div></div>
    <div class="card"><div class="photo" role="img" aria-label="体幹トレーニングの写真"></div><div class="card-body"><h3>体幹を鍛えたい方へ</h3><p>姿勢を支える筋肉を整え、疲れにくい体をつくります。</p></div></div>
    <div class="card"><div class="photo" role="img" aria-label="交通事故治療の写真"></div><div class="card-body"><h3>交通事故治療</h3><p>むち打ちなど事故後の不調を丁寧にケアします。</p></div></div>
    <div class="card"><div class="photo" role="img" aria-label="自費治療の写真"></div><div class="card-body"><h3>自費治療</h3><p>保険外の施術でより細やかに体を整えます。</p></div></div>
    <div class="card"><div class="photo" role="img" aria-label="枕と眠る女性の写真"></div><div class="card-body"><h3>オーダーメイド枕</h3><p>あなたに合う枕で快適な睡眠をサポートします。</p></div></div>
  </div>
  <div class="center"><span class="more-btn">その他の施術はこちら</span></div>
  <div class="contact-banner">
    <div class="cb-name"><div class="n">ともき鍼灸院・整骨院</div><div class="s">お気軽にお問い合わせください</div></div>
    <div class="cb-main">
      <div>
        <div class="cb-hours">受付時間 9:00〜12:00 / 15:00〜20:00<br>休診日 日曜・祝日</div>
        <div class="cb-tel"><svg width="20" height="20" viewBox="0 0 24 24"><path fill="currentColor" d="M6.6 10.8a15 15 0 0 0 6.6 6.6l2.2-2.2c.3-.3.7-.4 1-.2 1.1.4 2.3.6 3.6.6.6 0 1 .4 1 1V20c0 .6-.4 1-1 1A17 17 0 0 1 3 4c0-.6.4-1 1-1h3.5c.6 0 1 .4 1 1 0 1.3.2 2.5.6 3.6.1.3 0 .7-.2 1z"/></svg>0743-55-2680</div>
      </div>
      <div class="cb-btns"><div class="cb-btn">ご予約・お問い合わせ</div><div class="cb-btn">アクセス</div></div>
    </div>
    <div class="cb-photo" role="img" aria-label="院の外観写真"></div>
  </div>
</section>

<section class="concerns">
  <h2 class="sec-title">このような症状でお悩みではありませんか?</h2>
  <div class="concern-row">
    <div class="concern"><div class="photo" role="img" aria-label="首と肩の痛みに悩む人の写真"></div>首・肩の痛み</div>
    <div class="concern"><div class="photo" role="img" aria-label="疲れた様子の人の写真"></div>取れない疲れ</div>
    <div class="concern"><div class="photo" role="img" aria-label="眠れずにいる人の写真"></div>不眠</div>
  </div>
  <div class="concern-row">
    <div class="concern"><div class="photo" role="img" aria-label="腰を押さえる人の写真"></div>腰痛</div>
    <div class="concern"><div class="photo" role="img" aria-label="交通事故によるむち打ちの写真"></div>交通事故の痛み</div>
  </div>
</section>

<section class="voices">
  <h2 class="sec-title">患者様の声</h2>
  <div class="voice-box">
    <h3>肩こり、腰痛、腰部痛 40代 女性</h3>
    <p>長年の肩こりと腰の痛みに悩んでいましたが、丁寧に話を聞いてもらい自分に合った施術を受けられました。通うたびに体が軽くなり、今では毎日がとても楽です。院内も落ち着いていて安心して通えています。</p>
  </div>
  <div class="voice-people">
    <div class="photo" role="img" aria-label="患者様の写真"></div>
    <div class="photo" role="img" aria-label="患者様の写真"></div>
    <div class="photo" role="img" aria-label="患者様の写真"></div>
  </div>
  <div class="center"><span class="more-btn">もっと患者様の声を見る</span></div>
  <div class="contact-banner">
    <div class="cb-name"><div class="n">ともき鍼灸院・整骨院</div><div class="s">お気軽にお問い合わせください</div></div>
    <div class="cb-main">
      <div>
        <div class="cb-hours">受付時間 9:00〜12:00 / 15:00〜20:00<br>休診日 日曜・祝日</div>
        <div class="cb-tel"><svg width="20" height="20" viewBox="0 0 24 24"><path fill="currentColor" d="M6.6 10.8a15 15 0 0 0 6.6 6.6l2.2-2.2c.3-.3.7-.4 1-.2 1.1.4 2.3.6 3.6.6.6 0 1 .4 1 1V20c0 .6-.4 1-1 1A17 17 0 0 1 3 4c0-.6.4-1 1-1h3.5c.6 0 1 .4 1 1 0 1.3.2 2.5.6 3.6.1.3 0 .7-.2 1z"/></svg>0743-55-2680</div>
      </div>
      <div class="cb-btns"><div class="cb-btn">ご予約・お問い合わせ</div><div class="cb-btn">アクセス</div></div>
    </div>
    <div class="cb-photo" role="img" aria-label="院の外観写真"></div>
  </div>
</section>

<section class="posts">
  <div class="post-col">
    <h2>ブログ</h2>
    <ul>
      <li><span>2018.07.01</span>季節の変わり目の体調管理について</li>
      <li><span>2018.06.24</span>自宅でできる簡単ストレッチ</li>
      <li><span>2018.06.17</span>良い睡眠のための枕選び</li>
      <li><span>2018.06.10</span>デスクワークと肩こりの関係</li>
      <li><span>2018.06.03</span>体幹を整えると疲れにくくなる</li>
      <li><span>2018.05.27</span>産後の腰痛ケアについて</li>
    </ul>
    <div class="center"><span class="more-btn">ブログ一覧を見る</span></div>
  </div>
  <div class="post-col">
    <h2>お知らせ</h2>
    <ul>
      <li><span>2018.07.01</span>夏季休診日のお知らせ</li>
      <li><span>2018.06.20</span>受付時間変更のお知らせ</li>
      <li><span>2018.06.05</span>オーダーメイド枕の取扱い開始</li>
      <li><span>2018.05.28</span>ホームページをリニューアルしました</li>
      <li><span>2018.05.10</span>駐車場のご案内</li>
      <li><span>2018.04.29</span>連休中の診療について</li>
    </ul>
    <div class="center"><span class="more-btn">お知らせ一覧を見る</span></div>
  </div>
</section>

<section class="access">
  <div class="access-card">
    <p style="text-align:center;font-size:13px">ご予約・お問い合わせはこちら</p>
    <div class="access-tel"><svg width="24" height="24" viewBox="0 0 24 24"><path fill="currentColor" d="M6.6 10.8a15 15 0 0 0 6.6 6.6l2.2-2.2c.3-.3.7-.4 1-.2 1.1.4 2.3.6 3.6.6.6 0 1 .4 1 1V20c0 .6-.4 1-1 1A17 17 0 0 1 3 4c0-.6.4-1 1-1h3.5c.6 0 1 .4 1 1 0 1.3.2 2.5.6 3.6.1.3 0 .7-.2 1z"/></svg>0743-55-2680</div>
    <table class="hours">
      <tr><th>受付時間</th><th>月</th><th>火</th><th>水</th><th>木</th><th>金</th><th>土</th><th>日</th></tr>
      <tr><td>9:00〜12:00</td><td>●</td><td>●</td><td>●</td><td>●</td><td>●</td><td>●</td><td>×</td></tr>
      <tr><td>15:00〜20:00</td><td>●</td><td>●</td><td>●</td><td>×</td><td>●</td><td>▲</td><td>×</td></tr>
    </table>
    <p style="font-size:11px;color:var(--muted);margin-top:8px">▲土曜午後は17:00まで　休診日：日曜・祝日</p>
  </div>
  <div class="map" role="img" aria-label="院周辺の地図"></div>
</section>

<footer class="footer">
  <div class="f-info">
    <div class="logo"><span class="mark"></span>ともき鍼灸院・整骨院</div>
    <p>〒000-0000<br>架空県緑野市中央町1-2-3<br>TEL 0743-55-2680</p>
    <span class="f-btn">ご予約・お問い合わせ</span>
    <div class="f-talq"><i></i>TALQ</div>
  </div>
  <div class="f-links">
    <a href="#">当院について</a><a href="#">交通事故治療</a><a href="#">よくあるご質問</a>
    <a href="#">施術メニューと料金</a><a href="#">オーダーメイド枕</a><a href="#">お問い合わせ</a>
    <a href="#">首・肩の痛み</a><a href="#">自費治療</a><a href="#">ブログ</a>
    <a href="#">取れない疲れ</a><a href="#">鍼灸治療</a><a href="#">お知らせ</a>
    <a href="#">不眠・腰痛</a><a href="#">患者様の声</a><a href="#">体幹を鍛えたい方へ</a>
  </div>
  <div class="f-social"><span>Friendvio</span><span>Picturely</span><span>TALQ</span></div>
  <div class="copy">© ともき鍼灸院・整骨院</div>
</footer>

</body>
</html>
```